Outdoor group training business needs advertising banner

Already have logo, need banner to advertise coming business. Red and black lettering on white, same colour red as logo.
Items to include :
Logo : Kravenly Fitness
The outdoor group training specialists
T : 0472 815 604
E : kravenly@mailbarrow.com
W : kravenlyfitness.com.au
Outdoor group training based at Lindenvale Rowers Club coming soon.
Starting Monday 6th Janurary 2014.
Secure your place now as class numbers are limited.
Check out our website or call Gareth on 0472 815 604 for more information.
All trainers are registered with Motion Registry and accredited by Drillfield Council.

Requirements
Must have
• Logo (red&black)
Aiming for about A1 size or larger.

```html
<!DOCTYPE html>
<html lang="en">
<head>
<meta charset="utf-8">
<title>Kravenly Fitness – Outdoor Group Training</title>
<link rel="stylesheet" href="https://fonts.googleapis.com/css2?family=PT+Sans:wght@400;700&family=Questrial&family=Open+Sans:wght@700;800&display=swap">
<style>
  :root {
    --brand-red: #e8432e;
    --accent-orange: #e4593d;
    --ink: #1f1f1f;
    --shadow-grey: #d4d4d6;
    --badge-grey: #5b5b5e;
    --paper: #ffffff;
  }
  * { margin: 0; padding: 0; box-sizing: border-box; }
  html, body { width: 875px; height: 1200px; overflow: hidden; background: var(--paper); }
  .flyer {
    position: relative;
    width: 875px; height: 1200px;
    background: var(--paper);
    font-family: "PT Sans", sans-serif;
    color: var(--ink);
    overflow: hidden;
  }
  .corner { position: absolute; left: 0; top: 0; width: 875px; height: 1200px; }
  .headline {
    position: absolute; left: 39px; top: 236px;
    font-family: "PT Sans", sans-serif; font-weight: 400;
    font-size: 37px; line-height: 48.5px;
    color: var(--brand-red);
  }
  .hero { position: absolute; left: 0; top: 0; }
  .tagline-band {
    position: absolute; left: 32px; top: 702px;
    width: 804px; height: 60px;
    background: var(--accent-orange);
    color: var(--paper);
    font-family: "Questrial", sans-serif;
    font-size: 39px; line-height: 60px;
    padding-left: 13px; letter-spacing: 0.5px;
    white-space: nowrap;
  }
  .call-to-action {
    position: absolute; left: 32px; top: 788px;
    font-size: 31px; white-space: nowrap;
  }
  .call-to-action strong { color: var(--accent-orange); font-weight: 700; }
  .details {
    position: absolute; left: 32px; top: 841px;
    font-size: 21.5px; line-height: 33px; white-space: nowrap;
  }
  .details strong { font-weight: 700; }
  .start-date {
    position: absolute; left: 32px; top: 995px;
    font-family: "Open Sans", sans-serif; font-weight: 700;
    font-size: 33px; letter-spacing: 1.5px; white-space: nowrap;
  }
  .brand-name {
    position: absolute; left: 32px; top: 1122px;
    display: flex; align-items: center; gap: 10px;
    font-family: "PT Sans", sans-serif; font-weight: 700;
    font-size: 28px; color: var(--brand-red); white-space: nowrap;
  }
  .brand-name .dot { width: 30px; height: 30px; border-radius: 50%; background: var(--brand-red); }
  .contact { position: absolute; left: 409px; top: 1114px; list-style: none; font-size: 22px; line-height: 33px; }
  .contact li { display: flex; align-items: center; gap: 8px; white-space: nowrap; }
  .contact svg { width: 17px; height: 17px; flex: none; }
</style>
</head>
<body>
<main class="flyer">
  <svg class="corner" viewBox="0 0 875 1200" aria-hidden="true">
    <polygon points="0,160 0,172 58,197 62,186" fill="var(--shadow-grey)"/>
    <polygon points="0,0 165,0 58,185 0,160" fill="var(--accent-orange)"/>
    <polygon points="745,1094 875,1170 875,1186 741,1104" fill="var(--shadow-grey)"/>
    <polygon points="875,869 745,1094 875,1170" fill="var(--accent-orange)"/>
  </svg>

  <h1 class="headline">Outdoor<br>Group<br>Training<br>Based At<br>Lindenvale<br>Rowers<br>Club.</h1>

  <svg class="hero" width="875" height="1200" viewBox="0 0 875 1200">
    <defs>
      <linearGradient id="park" x1="0" y1="0" x2="0" y2="1">
        <stop offset="0" stop-color="#9fbf6a"/>
        <stop offset="0.45" stop-color="#7aa63f"/>
        <stop offset="1" stop-color="#5f8f2e"/>
      </linearGradient>
    </defs>
    <circle cx="552" cy="327" r="283" fill="url(#park)" stroke="var(--accent-orange)" stroke-width="4"
            role="img" aria-label="Photo: group of people doing lunges on park grass with a trainer in red"/>
    <g class="coming-soon">
      <circle cx="355" cy="561" r="84" fill="var(--badge-grey)" stroke="var(--accent-orange)" stroke-width="5"/>
      <g transform="rotate(-8 355 561)" font-family="Open Sans, sans-serif" font-weight="800" fill="#ffffff" text-anchor="middle" font-size="33">
        <text x="357" y="555">coming</text>
        <text x="357" y="596">soon</text>
      </g>
    </g>
  </svg>

  <p class="tagline-band">The Outdoor Group Training Specialists</p>

  <p class="call-to-action">Secure your place now as <strong>class numbers are limited.</strong></p>

  <p class="details">Check out our website or call&nbsp; Gareth on <strong>0472 815 604</strong> for more information.<br>All trainers are registered with Motion Registry and accredited by Drillfield<br>Council.</p>

  <p class="start-date">Starting Monday 6th January 2014.</p>

  <div class="brand-name"><span class="dot"></span>Kravenly Fitness</div>

  <ul class="contact">
    <li>
      <svg viewBox="0 0 20 20" aria-hidden="true"><rect x="1.5" y="4" width="17" height="12" fill="none" stroke="#333" stroke-width="1.5"/><polyline points="1.5,4 10,11 18.5,4" fill="none" stroke="#333" stroke-width="1.5"/></svg>
      kravenly@mailbarrow.com
    </li>
    <li>
      <svg viewBox="0 0 20 20" aria-hidden="true"><circle cx="10" cy="10" r="8.5" fill="none" stroke="#333" stroke-width="1.4"/><ellipse cx="10" cy="10" rx="3.8" ry="8.5" fill="none" stroke="#333" stroke-width="1.2"/><line x1="1.5" y1="10" x2="18.5" y2="10" stroke="#333" stroke-width="1.2"/><line x1="3" y1="5.5" x2="17" y2="5.5" stroke="#333" stroke-width="1"/><line x1="3" y1="14.5" x2="17" y2="14.5" stroke="#333" stroke-width="1"/></svg>
      kravenlyfitness.com.au
    </li>
  </ul>
</main>
</body>
</html>
```